Banners - Various shapes and sizes

I need a banner set for an event planning company, www.coralvowsandparties.example

This will be for their Brightlane Promo campaign, the banners can all look very similar but the final project is for a set of them, delivered as 1 PSD, in these shapes/sizes:

Mobile leaderboard: 320 x 50
Banner: 468 x 60
Leaderboard: 728 x 90
Square: 250 x 250
Small square: 200 x 200
Large rectangle: 336 x 280
Inline rectangle: 300 x 250
Skyscraper: 120 x 600
Wide skyscraper: 160 x 600
Half-page: 300 x 600
Large leaderboard: 970x90

At a minimum, they should include:

- The Lantern Hall Events logo
- Color scheme from their website
- Phone # and call to action

Looking over their site can provide some information on the venues, wedding packages, and awards received to get an idea of who Lantern Hall Events is.
Updates

Target Market(s)

Newly engaged brides

Industry/Entity Type

Event Planning

Requirements
Must have
• At a minimum, they should include:

- The Lantern Hall Events logo (I have attached it here)

```html
<!DOCTYPE html>
<html lang="en">
<head>
<meta charset="utf-8">
<title>Lantern Hall Events – Large Rectangle Banner</title>
<link rel="stylesheet" href="https://fonts.googleapis.com/css2?family=Montserrat:wght@400;500;600&family=PT+Sans+Narrow:wght@400;700&display=swap">
<style>
  :root {
    --page-bg: #495057;
    --sky-top: #63cdef;
    --sky-low: #a9e6f6;
    --sea: #5cc6e2;
    --sea-far: #3aa9cf;
    --sand: #e9e2d6;
    --sand-dark: #d8cdbd;
    --headline: #0f5f95;
    --bullet: #ffffff;
    --magenta: #c2307f;
    --pink-band: #d36aa5;
    --pink-band-light: #e7a8cb;
    --panel: #ffffff;
  }
  * { margin: 0; padding: 0; box-sizing: border-box; }
  html, body {
    width: 1200px;
    height: 900px;
    overflow: hidden;
    background: var(--page-bg);
  }
  .banner {
    position: absolute;
    left: 348px;
    top: 240px;
    width: 504px;
    height: 420px;
    overflow: hidden;
    background: var(--panel);
  }
  .banner__photo {
    position: absolute;
    inset: 0;
    background: linear-gradient(
      to bottom,
      var(--sky-top) 0%,
      var(--sky-low) 33%,
      var(--sea-far) 36%,
      var(--sea) 48%,
      var(--sky-low) 56%,
      var(--sand) 62%,
      var(--sand-dark) 80%
    );
  }
  .banner__wave {
    position: absolute;
    inset: 0;
    width: 504px;
    height: 420px;
  }
  .banner__headline {
    position: absolute;
    left: 27px;
    top: 16px;
    font-family: "Montserrat", sans-serif;
    font-weight: 500;
    font-size: 35px;
    line-height: 46px;
    color: var(--headline);
    letter-spacing: -0.2px;
  }
  .banner__features {
    position: absolute;
    left: 27px;
    top: 116px;
    list-style: none;
    font-family: "PT Sans Narrow", sans-serif;
    font-weight: 700;
    font-size: 22px;
    line-height: 32px;
    color: var(--bullet);
    text-shadow: 0 1px 2px rgba(0, 60, 100, 0.35);
  }
  .banner__cta {
    position: absolute;
    left: 27px;
    top: 237px;
    width: 220px;
    height: 53px;
    border-radius: 3px;
    background: var(--magenta);
    color: #fff;
    font-family: "Montserrat", sans-serif;
    font-weight: 600;
    font-size: 19px;
    line-height: 53px;
    text-align: center;
  }
  .banner__brand {
    position: absolute;
    left: 15px;
    top: 350px;
    font-family: "Montserrat", sans-serif;
    font-weight: 500;
    font-size: 31px;
    line-height: 44px;
    color: var(--magenta);
  }
</style>
</head>
<body>
  <div class="banner">
    <div class="banner__photo" role="img" aria-label="Bride and groom dressed in white standing on a sunny beach looking out at a turquoise sea"></div>

    <svg class="banner__wave" viewBox="0 0 504 420" aria-hidden="true">
      <path d="M0,280 Q230,338 504,326 L504,350 Q240,356 0,298 Z" fill="var(--pink-band)"/>
      <path d="M0,298 Q240,356 504,350 L504,358 Q240,362 0,306 Z" fill="var(--pink-band-light)"/>
      <path d="M0,306 Q240,362 504,358 L504,420 L0,420 Z" fill="var(--panel)"/>
    </svg>

    <h1 class="banner__headline">Weddings, Quinces<br>&amp; Corp Events</h1>

    <ul class="banner__features">
      <li>Customized wedding packages</li>
      <li>Beautiful Miami locations</li>
      <li>Voted #1 in Miami</li>
    </ul>

    <div class="banner__cta">Call 305 555 0148</div>

    <div class="banner__brand">Lantern Hall Events</div>
  </div>
</body>
</html>
```